Vellmora Harvest Online organic artisan and gourmet supermarket

Brief:
Brand: Vellmora Harvest (VH) is an online store selling artisan and organinc Italian products. Our look and feel we have gone with is rustic, premium and unfiltered (visit us @ www.vellmoraharvest.com.au)
Our slogan: "cook Italy, eat Italy, love Italy"
Goals: prior to our online store going live, we used to attend a food market once a week. Due to unfortunate circumstances, we stopped. Since then, our store has gone live and wanted to use the card as a reminder we are back at the markets.
I also have a restaurant, "vellmora ristorante" so I wanted to hand them out to customers in the restaurant but also act as reminder of our pop up market stores and our website to buy from.
Personality: VH is more than just a store. Our goal is to be not only a store but an informationa hub of Italian food.
We offer assistance to people who need help in their kitchen as well as catering
Logo: I have a logo which I was not able to upload.

Target Market(s)

Food lovers
Italian food interest
Wealthy
Organic gourmet food enthusiest

Industry/Entity Type

Store

Contact Information for Business Card

Shop online or visit us @ Birchwell Hollow organic market
Ciao@vellmoraharvest.com.au
Www.vellmoraharvest.com.au

Online store, Cooking advice, catering, ristorante and information hub

Requirements
Must have
• Logo
• Information
• May be larger than a business card to fit information but smaller than a post card
• Need to look interesting and different
• Not a simple card design
Nice to have
• Different fonts
• Rustic looking
• Qwerky

```html
<!DOCTYPE html>
<html lang="en">
<head>
<meta charset="utf-8">
<title>Vellmora Harvest – Business Card</title>
<link href="https://fonts.googleapis.com/css2?family=Lato:wght@400;700&display=swap" rel="stylesheet">
<style>
  :root {
    --backdrop: #e9e6e3;
    --card-top: #2f3b47;
    --card-bottom: #232d37;
    --ink-light: #ffffff;
    --ink-soft: #e6e9ec;
    --accent-red: #e8203f;
    --shadow: rgba(0, 0, 0, 0.28);
  }
  * { box-sizing: border-box; margin: 0; padding: 0; }
  html, body {
    width: 1200px;
    height: 900px;
    overflow: hidden;
    background: var(--backdrop);
    font-family: "Lato", "Helvetica Neue", Arial, sans-serif;
  }
  .stage { position: relative; width: 1200px; height: 900px; }

  .card {
    position: absolute;
    background: radial-gradient(ellipse at 60% 35%, var(--card-top) 0%, var(--card-bottom) 80%);
    box-shadow: 0 10px 30px var(--shadow);
    color: var(--ink-light);
  }
  .card--front { left: 238px; top: 62px; width: 555px; height: 342px; }
  .card--back  { left: 457px; top: 518px; width: 560px; height: 343px; }

  .brand-mark {
    position: absolute;
    display: flex;
    align-items: center;
    gap: 10px;
    white-space: nowrap;
  }
  .brand-mark__dot {
    width: 14px; height: 14px;
    border-radius: 50%;
    border: 2px solid var(--ink-light);
  }
  .brand-mark__name {
    font-size: 19px;
    font-weight: 400;
    letter-spacing: 1px;
    color: var(--ink-light);
  }
  .card--front .brand-mark { left: 52px; top: 122px; }
  .card--back  .brand-mark { left: 50%; top: 142px; transform: translateX(-50%); }

  .contact {
    position: absolute;
    right: 23px;
    top: 136px;
    text-align: right;
  }
  .contact__name {
    font-size: 18px;
    font-weight: 700;
    color: var(--accent-red);
    line-height: 1.1;
  }
  .contact__role {
    font-size: 15px;
    color: var(--ink-soft);
    margin-top: 2px;
  }
  .contact__lines { margin-top: 19px; }
  .contact__line {
    display: flex;
    justify-content: flex-end;
    align-items: center;
    gap: 8px;
    font-size: 15px;
    color: var(--ink-soft);
    line-height: 20px;
  }
  .contact__line svg { width: 10px; height: 10px; flex: none; }
  .contact__slogan {
    font-size: 15px;
    color: var(--ink-soft);
    margin-top: 14px;
    padding-right: 0;
  }

  .market-note {
    position: absolute;
    left: 40px;
    top: 284px;
    font-size: 19px;
    color: var(--ink-light);
  }

  .services {
    position: absolute;
    left: 0; right: 0;
    top: 278px;
    text-align: center;
    font-size: 15.5px;
    color: var(--ink-light);
  }
</style>
</head>
<body>
<main class="stage">

  <section class="card card--front" aria-label="Business card front">
    <div class="brand-mark">
      <span class="brand-mark__dot"></span>
      <span class="brand-mark__name">Vellmora Harvest</span>
    </div>

    <div class="contact">
      <p class="contact__name">Marco Ellison</p>
      <p class="contact__role">Managing Director</p>
      <div class="contact__lines">
        <p class="contact__line">Ciao@vellmoraharvest.com.au
          <svg viewBox="0 0 10 10" aria-hidden="true"><rect x="0.5" y="2" width="9" height="6.5" rx="1" fill="var(--accent-red)"/><path d="M1 2.6 L5 5.6 L9 2.6" stroke="var(--card-bottom)" stroke-width="0.9" fill="none"/></svg>
        </p>
        <p class="contact__line">Www.vellmoraharvest.com.au
          <svg viewBox="0 0 10 10" aria-hidden="true"><circle cx="5" cy="5" r="4.5" fill="var(--accent-red)"/><path d="M0.8 5 H9.2 M5 0.6 C3 3 3 7 5 9.4 M5 0.6 C7 3 7 7 5 9.4" stroke="var(--card-bottom)" stroke-width="0.7" fill="none"/></svg>
        </p>
      </div>
      <p class="contact__slogan">"cook Italy, eat Italy, love Italy"</p>
    </div>

    <p class="market-note">Shop online or visit us @ Birchwell Hollow organic market</p>
  </section>

  <section class="card card--back" aria-label="Business card back">
    <div class="brand-mark">
      <span class="brand-mark__dot"></span>
      <span class="brand-mark__name">Vellmora Harvest</span>
    </div>
    <p class="services">Online store | Cooking advice | catering | ristorante and information hub</p>
  </section>

</main>
</body>
</html>
```